We need a web site design that is connected to Talbrook Roofing an American company, Veteran owned. Specializing in new roofs of all kinds, repair existing roofs and emergency roof repairs. located in the north Georgia mountains

Target Market(s)

homeowners end users, real estate, home owners insurance companies

Industry/Entity Type

roofing

Contact Information for Business Card

logo, Veteran owned, supports veteran charities, phone number ect

Font styles to use
Serif

Requirements
Should not have
• na

```html
<!DOCTYPE html>
<html lang="en">
<head>
<meta charset="utf-8">
<title>Talbrook Roofing – Business Card</title>
<link rel="stylesheet" href="https://fonts.googleapis.com/css2?family=Roboto+Slab:wght@400;500;700&display=swap">
<style>
  :root {
    --bg: #ece7df;
    --gold-dark: #c8741f;
    --gold-mid: #d99a35;
    --gold-light: #e6c04e;
    --card-white: #efefef;
    --ink: #1d1d1d;
    --accent-gold: #d4912a;
    --brand-red: #c8261b;
    --band-red: #9c1a1e;
    --band-red-dark: #7e1417;
  }
  * { box-sizing: border-box; margin: 0; padding: 0; }
  html, body {
    width: 1200px; height: 1200px; overflow: hidden;
    background: var(--bg);
    font-family: "Roboto Slab", serif;
  }
  .canvas { position: relative; width: 1200px; height: 1200px; }

  .card {
    position: absolute;
    left: 206px;
    width: 786px;
    height: 450px;
    overflow: hidden;
    box-shadow: 0 6px 18px rgba(0,0,0,0.18);
  }

  /* Front */
  .card-front {
    top: 118px;
    background: linear-gradient(100deg, var(--gold-dark) 0%, var(--gold-mid) 50%, var(--gold-light) 100%);
  }
  .front-brand {
    position: absolute;
    left: 0; right: 0; top: 150px;
    text-align: center;
    color: var(--brand-red);
    font-weight: 700;
    font-size: 46px;
    line-height: 1.15;
    letter-spacing: 4px;
    text-transform: uppercase;
  }
  .front-tagline {
    position: absolute;
    left: 0; right: 0; top: 280px;
    text-align: center;
    color: var(--brand-red);
    font-weight: 700;
    font-size: 18px;
    letter-spacing: 5px;
    text-transform: uppercase;
  }

  /* Back */
  .card-back {
    top: 635px;
    background: var(--card-white);
  }
  .name-tab {
    position: absolute;
    left: 0; top: 100px;
    width: 20px; height: 48px;
    background: linear-gradient(180deg, var(--gold-light), var(--accent-gold));
    border-radius: 0 3px 3px 0;
  }
  .contact {
    position: absolute;
    left: 45px; top: 98px;
    color: var(--ink);
  }
  .person-name {
    color: var(--accent-gold);
    font-weight: 700;
    font-size: 27px;
    letter-spacing: 0.2px;
    line-height: 1.1;
  }
  .person-role {
    font-size: 17px;
    margin-top: 3px;
  }
  .address {
    font-size: 17px;
    line-height: 23px;
    margin-top: 18px;
  }
  .contact-list { list-style: none; margin-top: 10px; }
  .contact-list li {
    display: flex; align-items: center;
    font-size: 17px;
    height: 31px;
  }
  .contact-list svg { width: 18px; height: 18px; margin-right: 10px; flex: none; }

  .back-brand {
    position: absolute;
    left: 450px; width: 290px; top: 140px;
    text-align: center;
    color: var(--brand-red);
  }
  .back-brand-name {
    font-weight: 700;
    font-size: 36px;
    line-height: 1.15;
    letter-spacing: 3px;
    text-transform: uppercase;
  }
  .back-brand-tagline {
    margin-top: 10px;
    font-weight: 700;
    font-size: 15px;
    letter-spacing: 4px;
    text-transform: uppercase;
  }

  .footer-band { position: absolute; left: 0; bottom: 0; width: 786px; height: 42px; }
  .footer-note {
    position: absolute;
    right: 48px; bottom: 10px;
    color: #fff;
    font-weight: 700;
    font-size: 17px;
    letter-spacing: 0.2px;
  }
</style>
</head>
<body>
<main class="canvas">
  <section class="card card-front">
    <div class="front-brand">Talbrook<br>Roofing</div>
    <p class="front-tagline">Veteran Owned</p>
  </section>

  <section class="card card-back">
    <div class="name-tab"></div>
    <div class="contact">
      <h1 class="person-name">DANIEL WHITCOMBE</h1>
      <p class="person-role">Senior Project Manager</p>
      <p class="address">2150 Laurel Ridge Road<br>Blue Ridge, GA 30513, USA</p>
      <ul class="contact-list">
        <li>
          <svg viewBox="0 0 24 24" aria-hidden="true"><path fill="#d4912a" d="M6.6 10.8a15.1 15.1 0 0 0 6.6 6.6l2.2-2.2a1 1 0 0 1 1-.25 11.4 11.4 0 0 0 3.6.57 1 1 0 0 1 1 1V20a1 1 0 0 1-1 1A17 17 0 0 1 3 4a1 1 0 0 1 1-1h3.5a1 1 0 0 1 1 1c0 1.25.2 2.45.57 3.57a1 1 0 0 1-.25 1z"/></svg>
          +1 (706) 555-0148
        </li>
        <li>
          <svg viewBox="0 0 24 24" aria-hidden="true"><rect x="2" y="5" width="20" height="14" rx="1.5" fill="#d4912a"/><path d="M2.5 6l9.5 7 9.5-7" stroke="#fff" stroke-width="1.6" fill="none"/></svg>
          d.whitcombe@talbrookroofing.com
        </li>
        <li>
          <svg viewBox="0 0 24 24" aria-hidden="true"><g fill="none" stroke="#d4912a" stroke-width="2"><circle cx="12" cy="12" r="9"/><ellipse cx="12" cy="12" rx="4" ry="9"/><path d="M3 12h18M5 7h14M5 17h14"/></g></svg>
          www.talbrookroofing.com
        </li>
      </ul>
    </div>

    <div class="back-brand">
      <div class="back-brand-name">Talbrook<br>Roofing</div>
      <p class="back-brand-tagline">Veteran Owned</p>
    </div>

    <svg class="footer-band" viewBox="0 0 786 42" aria-hidden="true">
      <defs>
        <linearGradient id="bandGold" x1="0" x2="1" y1="0" y2="0">
          <stop offset="0" stop-color="#c8741f"/>
          <stop offset="1" stop-color="#e6c04e"/>
        </linearGradient>
        <linearGradient id="bandRed" x1="0" x2="1" y1="0" y2="0">
          <stop offset="0" stop-color="#9c1a1e"/>
          <stop offset="1" stop-color="#7e1417"/>
        </linearGradient>
      </defs>
      <polygon points="0,7 428,7 410,42 0,42" fill="url(#bandGold)"/>
      <polygon points="437,0 786,0 786,42 418,42" fill="url(#bandRed)"/>
    </svg>
    <p class="footer-note">We support veteran charities</p>
  </section>
</main>
</body>
</html>
```